TallFernSix needs some a graphic design ASAP. Visit https://tallfernsix.com/Home/About/ to get a feel for our current design. We need a visually pleasing way to add the information in the files attached to what already exists (the new sections are Reach, Discretion, and Heart).

This can either be a graphic with the information at the bottom or a redesign of the landing page. We'll accept whatever we like most.

I've attached some stock photos that I own / like. Feel free to use these directly or for inspiration. Icons are OK too. These are just an example.

```html
<!DOCTYPE html>
<html lang="en">
<head>
<meta charset="utf-8">
<title>TallFernSix – The world is your matchmaker</title>
<link rel="stylesheet" href="https://fonts.googleapis.com/css2?family=Roboto:wght@400;500;700&family=Roboto+Condensed:wght@400;700&display=swap">
<style>
  :root {
    --pink: #e8237a;
    --blue: #29b6e8;
    --dark: #2e313b;
    --dark-2: #3a3e4a;
    --page: #e7e8ea;
    --panel: #ffffff;
    --line: #dcdcdc;
    --text: #222;
    --muted: #555;
  }
  * { box-sizing: border-box; margin: 0; padding: 0; }
  html, body { width: 886px; height: 1200px; overflow: hidden; }
  body {
    position: relative;
    font-family: "Roboto", Arial, sans-serif;
    color: var(--text);
    background: linear-gradient(#e4e5e8 145px, #f4f4f5 700px, #ffffff 1136px);
  }
  .abs { position: absolute; }

  /* header */
  .site-header {
    position: absolute; left: 0; top: 0; width: 886px; height: 145px;
    background: radial-gradient(ellipse at 50% 120%, var(--dark-2), var(--dark) 70%);
    border-top: 4px solid var(--pink);
  }
  .utility-nav {
    position: absolute; left: 614px; top: 3px; width: 178px; height: 22px;
    background: var(--pink); border-radius: 0 0 12px 12px;
    display: flex; justify-content: center; gap: 18px; align-items: center;
    font: 700 11px "Roboto", Arial, sans-serif; color: #fff;
  }
  .brand { position: absolute; left: 36px; top: 36px; display: flex; align-items: center; gap: 10px; }
  .brand-mark { width: 44px; height: 44px; border-radius: 50%; background: var(--blue); }
  .brand-name { font: 700 34px "Roboto Condensed", Arial, sans-serif; color: var(--blue); line-height: 1; }
  .brand-tag { position: absolute; left: 136px; top: 78px; font-size: 10px; color: var(--blue); letter-spacing: .3px; }
  .tab {
    position: absolute; top: 112px; height: 33px;
    font: 700 16px "Roboto Condensed", Arial, sans-serif; text-transform: uppercase;
    display: flex; align-items: center; justify-content: center;
  }
  .tab-members { left: 30px; width: 95px; background: var(--pink); color: #fff; }
  .tab-about { left: 125px; width: 77px; background: #e7e8ea; color: #666; }
  .new-account {
    position: absolute; left: 692px; top: 108px; width: 160px; height: 37px;
    background: var(--pink); color: #fff; border-radius: 3px 3px 0 0;
    font: 700 14px "Roboto Condensed", Arial, sans-serif; letter-spacing: -.5px;
    display: flex; align-items: center; justify-content: flex-end; padding-right: 14px;
  }
  .new-account .avatar { position: absolute; left: 12px; top: 6px; width: 34px; height: 31px; background: #f8b7d2; border-radius: 14px 14px 0 0; }

  /* panels */
  .panel { position: absolute; background: var(--panel); border: 1px solid var(--line); border-radius: 3px; }
  .main-panel { left: 31px; top: 174px; width: 641px; height: 537px; }
  .headline { position: absolute; left: 0; width: 100%; top: 10px; text-align: center; font: 700 21px "Roboto", Arial, sans-serif; }
  .headline em { font-style: normal; color: var(--pink); }
  .flow { position: absolute; left: 0; top: 62px; width: 100%; height: 70px; }
  .flow-step { position: absolute; top: 0; width: 80px; font-size: 9.5px; line-height: 1.35; color: var(--text); }
  .flow-step svg { display: block; width: 40px; height: 36px; margin-bottom: 8px; }
  .flow-arrow { position: absolute; top: 13px; width: 12px; height: 12px; border-radius: 50%; background: #333; }
  .flow-arrow::after { content: ""; position: absolute; left: 4px; top: 3px; border: 3px solid transparent; border-left: 4px solid #fff; }
  .hero-art {
    position: absolute; left: 6px; top: 159px; width: 626px; height: 212px;
    background: linear-gradient(90deg, #f3c9d8 0%, var(--pink) 25%, var(--pink) 50%, var(--blue) 50%, var(--blue) 75%, #cfeaf5 100%);
  }
  .section-label { position: absolute; left: 0; width: 100%; top: 397px; text-align: center; font: 700 16px "Roboto", Arial, sans-serif; color: #444; }
  .referral-bar {
    position: absolute; left: 12px; top: 431px; width: 616px; height: 80px;
    border: 1px solid #c9c9c9; border-radius: 6px; background: linear-gradient(#fff, #f1f1f1);
    display: flex;
  }
  .referral-step { border-right: 1px solid #d6d6d6; display: flex; flex-direction: column; align-items: center; justify-content: flex-end; padding-bottom: 10px; font-size: 11.5px; color: #555; gap: 10px; }
  .referral-step:last-child { border-right: 0; }
  .referral-step svg { width: 36px; height: 32px; }
  .referral-step .star { color: var(--pink); }
  .referral-bar .flow-arrow { top: 31px; width: 20px; height: 20px; }
  .referral-bar .flow-arrow::after { left: 7px; top: 5px; border-width: 5px; border-left-width: 7px; }
  .fine-print { position: absolute; left: 25px; top: 521px; font-size: 9px; color: var(--pink); }

  .about-panel { left: 31px; top: 738px; width: 641px; height: 125px; }
  .panel-head { height: 35px; border-bottom: 1px solid var(--line); background: linear-gradient(#fff, #f5f5f5); padding-left: 16px; display: flex; align-items: center; font: 700 15px "Roboto Condensed", Arial, sans-serif; letter-spacing: -.6px; text-transform: uppercase; }
  .panel-head em { font-style: normal; color: var(--pink); }
  .about-body { padding: 12px 20px 0; font-size: 12.5px; line-height: 1.35; color: #222; }
  .about-body p + p { margin-top: 8px; }

  /* values */
  .value { position: absolute; top: 924px; width: 182px; }
  .value-icon { width: 56px; height: 56px; border-radius: 50%; margin: 0 auto; display: flex; align-items: center; justify-content: center; }
  .value-title { margin-top: 22px; text-align: center; font: 700 15px "Roboto", Arial, sans-serif; }
  .value-rule { margin-top: 15px; border-top: 1px solid #bbb; }
  .value-text { margin-top: 14px; font-size: 11.5px; line-height: 1.1; color: #333; }
  .is-blue .value-icon { background: var(--blue); } .is-blue .value-title { color: var(--blue); }
  .is-pink .value-icon { background: var(--pink); } .is-pink .value-title { color: var(--pink); }

  /* sidebar */
  .featured { left: 689px; top: 174px; width: 165px; height: 212px; }
  .side-head { height: 35px; border-bottom: 1px solid var(--line); display: flex; align-items: center; justify-content: center; font: 700 15px "Roboto Condensed", Arial, sans-serif; letter-spacing: -.7px; text-transform: uppercase; }
  .side-head em { font-style: normal; color: var(--pink); }
  .member-card { position: absolute; left: 34px; top: 47px; width: 98px; height: 141px; border: 1px solid #333; text-align: center; font-size: 11px; line-height: 1.2; color: #333; }
  .member-photo { width: 96px; height: 99px; background: linear-gradient(#6b4a3a, #c89a85); margin-bottom: 3px; }
  .member-name { color: #b0287a; }
  .share { left: 689px; top: 413px; width: 165px; height: 174px; }
  .share-list { list-style: none; padding: 17px 0 0 30px; }
  .share-list li { display: flex; align-items: center; gap: 12px; height: 28px; margin-bottom: 8px; color: var(--blue); font-size: 14px; }
  .share-list .mark { width: 28px; height: 28px; background: #3b5b9a; }
  .share-list li:nth-child(2) .mark { background: var(--blue); }
  .share-list li:nth-child(3) .mark { background: #2f86b8; }

  .site-footer {
    position: absolute; left: 0; top: 1136px; width: 886px; height: 64px; background: var(--dark);
    text-align: center; color: #fff; font-size: 14px; padding-top: 16px; line-height: 1.2;
  }
  .site-footer a { color: var(--pink); }
</style>
</head>
<body>
<header class="site-header">
  <nav class="utility-nav"><span>Log In</span><span>About</span><span>Contact</span></nav>
  <div class="brand"><span class="brand-mark"></span><span class="brand-name">TallFernSix</span></div>
  <div class="brand-tag">The world is your matchmaker.</div>
  <div class="tab tab-members">Members</div>
  <div class="tab tab-about">About</div>
  <div class="new-account"><span class="avatar"></span>NEW ACCOUNT</div>
</header>

<section class="panel main-panel">
  <h1 class="headline">You <em>CAN</em> Hurry Love!</h1>
  <div class="flow">
    <div class="flow-step" style="left:30px"><svg viewBox="0 0 40 36"><rect x="2" y="4" width="28" height="20" fill="none" stroke="#e8237a" stroke-width="2"/><rect x="6" y="9" width="20" height="10" fill="#29b6e8"/><path d="M31 14l8 8-4 0 2 5-2 1-2-5-3 3z" fill="#29b6e8"/></svg>Post a<br>Reward</div>
    <div class="flow-arrow" style="left:128px"></div>
    <div class="flow-step" style="left:150px"><svg viewBox="0 0 40 36"><circle cx="11" cy="22" r="9" fill="none" stroke="#e8237a" stroke-width="3"/><circle cx="29" cy="22" r="9" fill="none" stroke="#e8237a" stroke-width="3"/><path d="M4 15q6-12 14-4M22 11q8-8 14 4" fill="#29b6e8"/></svg>Be Seen</div>
    <div class="flow-arrow" style="left:247px"></div>
    <div class="flow-step" style="left:252px"><svg viewBox="0 0 40 36"><circle cx="12" cy="10" r="5" fill="#29b6e8"/><circle cx="28" cy="10" r="5" fill="#29b6e8"/><circle cx="20" cy="14" r="5" fill="#29b6e8"/><path d="M4 32q8-18 16 0M20 32q8-18 16 0" fill="#29b6e8"/></svg>Matchmakers<br>Compete</div>
    <div class="flow-arrow" style="left:353px"></div>
    <div class="flow-step" style="left:357px"><svg viewBox="0 0 40 36"><path d="M8 8h8l-2 12h-4zM22 10h8l-2 12h-4z" fill="#29b6e8"/><path d="M12 20v12M26 22v10" stroke="#e8237a" stroke-width="2"/><circle cx="20" cy="4" r="2.5" fill="#e8237a"/></svg>Schedule a<br>Date</div>
    <div class="flow-arrow" style="left:446px"></div>
    <div class="flow-step" style="left:455px"><svg viewBox="0 0 40 36"><path d="M12 32C2 24 2 14 8 12s6 4 4 4 0-8 6-4 0 12-6 20z" fill="#e8237a"/><path d="M24 26c8-6 12-14 8-18s-8 0-8 0-4-4-8 0 0 12 8 18z" fill="none" stroke="#e8237a" stroke-width="2"/></svg>Repeat as<br>Necessary</div>
    <div class="flow-arrow" style="left:551px"></div>
    <div class="flow-step" style="left:560px"><svg viewBox="0 0 40 36"><circle cx="13" cy="16" r="12" fill="#29b6e8"/><circle cx="27" cy="18" r="11" fill="none" stroke="#e8237a" stroke-width="3"/><path d="M27 24l-5-5a3 3 0 0 1 5-3 3 3 0 0 1 5 3z" fill="#29b6e8"/></svg>Success!</div>
  </div>
  <div class="hero-art" role="img" aria-label="Illustration of a woman and a man each lying on their stomach using a laptop, facing each other across pink and blue panels with a heart between them"></div>
  <h2 class="section-label">KNOW SOMEONE SINGLE?</h2>
  <div class="referral-bar">
    <div class="referral-step" style="width:116px"><svg viewBox="0 0 36 32"><rect x="2" y="6" width="32" height="22" fill="#29b6e8"/><path d="M2 6l16 12 16-12z" fill="#e8237a"/></svg>Send a Message</div>
    <div class="flow-arrow" style="left:106px"></div>
    <div class="referral-step" style="width:118px"><svg viewBox="0 0 36 32"><rect x="2" y="12" width="32" height="18" fill="#29b6e8"/><path d="M2 12l16-10 16 10-16 10z" fill="#e8237a"/><rect x="10" y="6" width="16" height="12" fill="#fff"/></svg>Get a Response</div>
    <div class="flow-arrow" style="left:225px"></div>
    <div class="referral-step" style="width:149px"><svg viewBox="0 0 36 32"><circle cx="10" cy="8" r="6" fill="#29b6e8"/><circle cx="26" cy="8" r="6" fill="#e8237a"/><path d="M0 30q10-22 20 0zM16 30q10-22 20 0z" fill="#29b6e8"/></svg>Make an Introduction</div>
    <div class="flow-arrow" style="left:373px"></div>
    <div class="referral-step" style="width:106px"><svg viewBox="0 0 36 32"><circle cx="18" cy="16" r="14" fill="none" stroke="#29b6e8" stroke-width="3"/><path d="M12 16l5 5 8-9" fill="none" stroke="#e8237a" stroke-width="2.5"/></svg>Wait</div>
    <div class="flow-arrow" style="left:479px"></div>
    <div class="referral-step" style="width:127px"><svg viewBox="0 0 36 32"><rect x="3" y="8" width="24" height="20" fill="none" stroke="#29b6e8" stroke-width="2"/><text x="7" y="24" font-size="12" fill="#e8237a" font-family="Arial">$</text><path d="M18 22l14-16" stroke="#29b6e8" stroke-width="3"/></svg><span>Collect! <span class="star">*</span></span></div>
  </div>
  <p class="fine-print">*(Subject to site rules)</p>
</section>

<section class="panel about-panel">
  <h2 class="panel-head">What is&nbsp;<em>TallFernSix</em>?</h2>
  <div class="about-body">
    <p>TallFernSix is a marketplace for matchmakers. Single? Post a profile so matchmakers can compete to find your perfect match. Know somebody single? You could get paid for setting them up!</p>
    <p>No algorithms. No profile browsing ad nauseam. Just real human matchmakers. TallFernSix is online dating for an offline world.</p>
  </div>
</section>

<section class="value is-blue" style="left:54px">
  <div class="value-icon"><svg width="40" height="40" viewBox="0 0 40 40"><circle cx="20" cy="20" r="17" fill="#fff"/><circle cx="20" cy="20" r="14" fill="none" stroke="#29b6e8" stroke-width="2"/><path d="M6 20h28M20 6v28" stroke="#29b6e8" stroke-width="2"/></svg></div>
  <h3 class="value-title">REACH</h3><div class="value-rule"></div>
  <p class="value-text">Human matchmakers have friends, family, co-workers and aquaintanc-es. When has an algorithm set you up with its cousin?</p>
</section>
<section class="value is-pink" style="left:274px">
  <div class="value-icon"><svg width="34" height="30" viewBox="0 0 34 30"><path d="M17 29C3 19 0 12 3 6s11-6 14 1c3-7 11-7 14-1s0 13-14 23z" fill="#fff"/></svg></div>
  <h3 class="value-title">HEART</h3><div class="value-rule"></div>
  <p class="value-text">If no matchmakers succed in finding you a match, your reward will be donated to a charity of your choice.</p>
</section>
<section class="value is-blue" style="left:493px">
  <div class="value-icon"><svg width="40" height="40" viewBox="0 0 40 40"><circle cx="20" cy="20" r="15" fill="#fff"/><circle cx="20" cy="20" r="8" fill="#3c9e8e"/><circle cx="20" cy="20" r="3.5" fill="#fff"/></svg></div>
  <h3 class="value-title">DISCRETION</h3><div class="value-rule"></div>
  <p class="value-text">Register with a private profile and reveal yourself only to matchmakers you choose.</p>
</section>

<aside class="panel featured">
  <h2 class="side-head">Featured Member</h2>
  <div class="member-card">
    <div class="member-photo" role="img" aria-label="Portrait photo of the featured member"></div>
    <div class="member-name">Dana</div><div>Texas</div><div>$1500</div>
  </div>
</aside>
<aside class="panel share">
  <h2 class="side-head">Spread the&nbsp;<em>Love</em></h2>
  <ul class="share-list">
    <li><span class="mark"></span>Chatterbook</li>
    <li><span class="mark"></span>Chirpline</li>
    <li><span class="mark"></span>NetLinker</li>
  </ul>
</aside>

<footer class="site-footer">
  <div><a>Terms of Use</a> | <a>Terms of Service</a> | <a>Learn More</a> | <a>Contact</a> | <a>Privacy Policy</a></div>
  <div>© 2011-2014 Tall Fern Six, LLC</div>
</footer>
</body>
</html>
```